Exhibition/ Conference Booth Design.

To design a background for our booth at an upcoming conference incorporating our logo. We're a market leader in the automation industry for lead-acid batteries. This includes UPS, automobiles, reserve power and traction. The design could be as simple as incorporating our logo into a design to fit our booth that shows we're forward-thinking, innovative future thinking or going into more detail about the different usages for lead-acid batteries.

*Market Leader
*R&D

Company Profile -

KWR is a market-leading supplier of Assembly and Plate Manufacturing equipment that is dedicated to helping businesses of all sizes thrive in today's ever-changing world. With our comprehensive range of products and services, our customer-centric approach, and our commitment to innovation, we are a proven, trusted partner for companies across the globe.

At KWR we are committed to our customers' success. That's why we work closely with them to understand their unique requirements, goals, and challenges, and tailor our solutions to meet their specific needs.

Innovation is at the heart of everything we do at KWR. We invest heavily in research and development to stay ahead of the curve, and we regularly introduce new features, upgrades, and solutions that anticipate our customers' evolving needs. Our commitment to innovation has earned us a reputation as a leader in the industry, and we are constantly exploring new technologies and trends to help our customers succeed.

Industry/Entity Type

Automation - Lead Acid - Engineering

Requirements
Must have
• Our Logo
Nice to have
• Hi All, some good potentials here but I’m wondering if I could update the brief to be more ‘green’ eco friendly - Incorporting where we use Lead Acid batteries. i.e Energy storage, reserve power, automobiles, traction wind/solar and the fact lead acid is widely recyclable. It would be good to see if any of you have some ideas of how to incorporate the logo into this also. Possibly doing something different with the logo colours also.

```html
<!DOCTYPE html>
<html lang="en">
<head>
<meta charset="utf-8">
<title>KWR Engineering – Green Eco Friendly Booth Backdrop</title>
<link rel="stylesheet" href="https://fonts.googleapis.com/css2?family=Anton&display=swap">
<style>
  :root {
    --brand-blue: #2a5ea8;
    --brand-blue-deep: #1d4f99;
    --eco-green: #62bd4f;
    --eco-green-light: #79c965;
    --ink: #0d0d0d;
    --paper: #ffffff;
    --factory-steel: #8d97a3;
    --factory-shadow: #4a5566;
  }
  html, body {
    margin: 0;
    padding: 0;
    width: 1200px;
    height: 1200px;
    overflow: hidden;
    background: var(--paper);
  }
  .backdrop {
    position: relative;
    width: 1200px;
    height: 1200px;
    background: var(--paper);
    overflow: hidden;
    font-family: "Anton", "Impact", sans-serif;
  }
  .backdrop-shapes {
    position: absolute;
    inset: 0;
    width: 1200px;
    height: 1200px;
  }
  .brand {
    position: absolute;
    top: 62px;
    right: 70px;
    text-align: right;
    color: var(--brand-blue);
    line-height: 1;
  }
  .brand-name {
    display: block;
    font-size: 112px;
    letter-spacing: 4px;
  }
  .brand-tagline {
    display: block;
    font-size: 34px;
    letter-spacing: 3px;
    margin-top: 6px;
  }
  .message {
    position: absolute;
    right: 70px;
    top: 712px;
    text-align: right;
    color: var(--ink);
    text-transform: uppercase;
  }
  .message-title {
    margin: 0;
    font-family: "Anton", "Impact", sans-serif;
    font-weight: 400;
    font-size: 80px;
    line-height: 70px;
    letter-spacing: 1px;
  }
  .message-uses {
    margin: 18px 0 0;
    font-size: 35px;
    line-height: 46px;
    letter-spacing: 0.5px;
  }
  .accent-bar {
    position: absolute;
    top: 1059px;
    height: 58px;
  }
  .accent-bar--blue {
    left: 172px;
    width: 318px;
    background: var(--brand-blue);
  }
  .accent-bar--white {
    left: 507px;
    width: 93px;
    background: var(--paper);
  }
</style>
</head>
<body>
<main class="backdrop">
  <svg class="backdrop-shapes" viewBox="0 0 1200 1200" xmlns="http://www.w3.org/2000/svg">
    <defs>
      <linearGradient id="factoryTone" x1="0" y1="0" x2="0.6" y2="1">
        <stop offset="0" stop-color="#b9c1cb"/>
        <stop offset="0.5" stop-color="var(--factory-steel)"/>
        <stop offset="1" stop-color="var(--factory-shadow)"/>
      </linearGradient>
      <linearGradient id="ecoTone" x1="0" y1="0" x2="0.4" y2="1">
        <stop offset="0" stop-color="var(--eco-green-light)"/>
        <stop offset="1" stop-color="var(--eco-green)"/>
      </linearGradient>
    </defs>

    <path class="factory-photo" role="img"
          aria-label="Photo: engineers in blue workwear at assembly stations on a battery plant factory floor"
          d="M0 0 H638 L975 370 L450 915 Q405 964 340 964 H0 Z"
          fill="url(#factoryTone)"/>

    <polygon class="side-wedge" points="0,699 0,948 119,824" fill="var(--brand-blue)"/>

    <path class="eco-panel" role="img"
          aria-label="Photo with green tint: smiling engineer in the workshop"
          d="M930 368 H1200 V1200 H418 V900 Q418 870 440 845 L880 390 Q900 368 930 368 Z"
          fill="url(#ecoTone)"/>

    <rect class="corner-diamond" x="892" y="287" width="136" height="136" rx="24"
          transform="rotate(45 960 355)" fill="var(--brand-blue-deep)" opacity="0.88"/>
  </svg>

  <div class="brand">
    <span class="brand-name">KWR</span>
    <span class="brand-tagline">ENGINEERING</span>
  </div>

  <section class="message">
    <h1 class="message-title">‘Green’ Eco<br>Friendly</h1>
    <p class="message-uses">Energy storage, reserve<br>power, automobiles, traction<br>wind/solar and the fact lead<br>acid is widely recyclable</p>
  </section>

  <div class="accent-bar accent-bar--blue"></div>
  <div class="accent-bar accent-bar--white"></div>
</main>
</body>
</html>
```